Travel agency website refresh

I want to refresh and simplify my current Wordpress.com website. Same general color scheme but modernize and make it user friendly for all devices. Must work with Wordpress. No live booking engines. We are a boutique luxury travel agency. Think luxury, vacation, boho chic, elegant, lush, tropical, cruises, first class. Romance and adventure.
Updates

I’ve guaranteed the project so I’m hoping to see more quality entries to make a decision

Target Market(s)

Luxury travelers

Industry/Entity Type

Travel

Coding

Coded - Design and coding required

Number of Pages Required

5+ page

Font styles to use
Sans Serif

Colors
0094D4
00A9DD
6FCCEA
C7EBF8
E9F6FB

Requirements
Must have
• Compatible with Wordpress.com, homepage, about page, contact page, faq page
Nice to have
• The homepage should quickly tell the consumer the type of travel I specialize in. My current website has this (journeywithmerel.example). I’d like to incorporate the about me as a preview on the home page.
Should not have
• Harsh colors, look generic

```html
<!DOCTYPE html>
<html lang="en">
<head>
<meta charset="utf-8">
<title>Journey with Merel — Luxury Travel</title>
<link href="https://fonts.googleapis.com/css2?family=Bellefair&family=Arimo:wght@400;700&display=swap" rel="stylesheet">
<style>
:root{
  --blue:#0094D4;--sky:#00A9DD;--teal:#6FCCEA;--accent:#5cc2cf;--pale:#C7EBF8;--mist:#E9F6FB;
  --ink:#1d1d1d;--grey:#6b6b6b;--white:#fff;
}
*{box-sizing:border-box;margin:0;padding:0}
html,body{width:1200px;height:4338px;overflow:hidden}
body{position:relative;font-family:"Arimo",Arial,sans-serif;color:var(--ink);background:var(--white)}
.abs{position:absolute}
.eyebrow{position:absolute;left:0;width:100%;text-align:center;font-size:12px;letter-spacing:6px;color:var(--accent)}
.heading{position:absolute;left:0;width:100%;text-align:center;font-family:"Bellefair",Georgia,serif;font-size:58px;line-height:1;color:var(--ink)}
/* hero */
.hero{position:absolute;left:0;top:0;width:1200px;height:660px;background:linear-gradient(180deg,#31556d 0%,#4f86a0 18%,#3f8aa0 32%,#3b7b73 48%,#4e6f3a 62%,#3f5a2f 75%,#dfe8ea 92%,#fff 100%)}
.nav{position:absolute;top:42px;font-size:10.5px;color:var(--white);white-space:nowrap}
.nav.active{color:var(--teal)}
.nav.active::after{content:"";position:absolute;left:50%;top:18px;width:3px;height:3px;margin-left:-1.5px;border-radius:50%;background:var(--teal)}
.brand{position:absolute;text-align:center;color:var(--white);font-family:"Arimo",sans-serif;font-weight:700}
.social{position:absolute;top:41px;width:18px;height:18px;border-radius:50%;background:rgba(255,255,255,.25)}
.btn-outline{position:absolute;left:960px;top:25px;width:118px;height:46px;border:1px solid rgba(255,255,255,.8);color:var(--white);font-size:11px;display:flex;align-items:center;justify-content:center}
.tagline{position:absolute;top:164px;left:0;width:100%;text-align:center;color:var(--white);font-size:13px;letter-spacing:6px}
.hero-title{position:absolute;top:178px;left:0;width:100%;text-align:center;font-family:"Bellefair",serif;font-weight:400;font-size:150px;line-height:1;background:linear-gradient(180deg,#3fd0d6 0%,#aee8ea 60%,#fff 100%);-webkit-background-clip:text;background-clip:text;color:transparent}
.search{position:absolute;left:145px;top:636px;width:910px;height:91px;background:var(--white);box-shadow:0 8px 24px rgba(0,0,0,.12);display:flex}
.field{position:relative;height:100%;border-right:1px solid #e3e3e3;padding:24px 0 0 0}
.field .lbl{font-size:10px;color:#9aa7ad;display:flex;align-items:center;gap:5px}
.field .lbl i{display:inline-block;width:10px;height:10px;background:var(--teal);border-radius:2px}
.field .val{font-size:12px;color:var(--ink);margin-top:10px}
.btn-teal{position:absolute;background:var(--accent);color:var(--white);font-size:12px;display:flex;align-items:center;justify-content:center}
/* about */
.about-text{position:absolute;left:225px;width:750px;text-align:center;font-size:11.5px;line-height:21px;color:var(--grey)}
.about-card{position:absolute;left:183px;top:1100px;width:335px;height:285px;border:2px solid var(--pale);background:var(--mist)}
.about-card h3{position:absolute;left:24px;top:22px;font-family:"Bellefair",serif;font-weight:400;font-size:19px;line-height:24px;color:var(--ink)}
.about-card p{position:absolute;left:24px;top:100px;width:230px;font-size:11px;line-height:21px;color:#8a969b}
.about-photo{position:absolute;left:461px;top:1135px;width:555px;height:308px;background:linear-gradient(180deg,#9ec7df 0%,#b7d6e4 25%,#3f95b5 50%,#1f7b9e 100%);box-shadow:0 20px 40px rgba(0,0,0,.15)}
/* destinations */
.dest{position:absolute;left:0;top:1545px;width:1200px;height:656px;background:linear-gradient(90deg,#2f2219 0%,#4a3526 30%,#3a2a1f 55%,#4b3627 80%,#2e2118 100%)}
.dest .eyebrow{top:82px;color:var(--teal)}
.dest .heading{top:105px;color:var(--white)}
.dcard{position:absolute;overflow:hidden}
.dcard span{position:absolute;left:0;bottom:26px;width:100%;text-align:center;color:var(--white);font-size:16px}
.arrow{position:absolute;width:28px;height:28px;border-radius:50%;background:var(--white);display:flex;align-items:center;justify-content:center}
/* ready */
.ready{position:absolute;left:0;top:2201px;width:1200px;height:570px;background:linear-gradient(180deg,#2f5f8f 0%,#4a7da8 25%,#5d8fb5 45%,#2e5a78 60%,#c9d8df 78%,#fff 100%)}
.ready h2{position:absolute;left:0;top:90px;width:100%;text-align:center;font-family:"Bellefair",serif;font-weight:400;font-size:54px;line-height:64px;color:var(--white)}
/* blogs */
.blog{position:absolute;overflow:hidden;color:var(--white)}
.blog .t{position:absolute;left:13px;right:13px;font-size:12px;line-height:17px}
.blog .m{position:absolute;left:13px;font-size:10px;color:var(--teal)}
.arrow-teal{position:absolute;width:30px;height:30px;border-radius:50%;background:var(--accent);display:flex;align-items:center;justify-content:center}
/* insurance */
.insure{position:absolute;left:0;top:3298px;width:1200px;height:767px;background:linear-gradient(180deg,#fff 0%,#eef3f2 8%,#c9d7d6 18%,#8fa8a4 26%,#6f8f93 36%,#5f8896 55%,#6a95a2 75%,#b9c9c6 100%)}
.insure .eyebrow{top:212px;color:#333}
.insure .heading{top:237px;color:#1f2a2e;font-size:60px}
.form{position:absolute;left:253px;top:312px;width:693px;height:380px;background:rgba(72,112,126,.82)}
.form h4{position:absolute;left:35px;top:28px;font-weight:400;font-size:17px;color:var(--white)}
.flabel{position:absolute;font-size:9.5px;color:var(--white);white-space:nowrap}
.input{position:absolute;height:41px;background:var(--white);font-size:11px;color:#8d8d8d;display:flex;align-items:center;padding-left:32px}
.box{position:absolute;width:40px;height:40px;border:1px solid rgba(255,255,255,.8)}
.radio{display:inline-block;width:9px;height:9px;border-radius:50%;border:1px solid #fff;vertical-align:-1px;margin-right:4px}
.badge{position:absolute;width:191px;height:42px;background:#2f69c8;border-radius:2px}
.badge::after{content:"";position:absolute;right:0;top:0;width:52px;height:42px;background:#f4f4f4}
/* footer */
.footer{position:absolute;left:0;top:4065px;width:1200px;height:273px;background:linear-gradient(90deg,#2e3135 0%,#4a4e52 30%,#3d4044 60%,#34373b 100%)}
.fcol-title{position:absolute;font-family:"Bellefair",serif;font-size:16px;color:var(--white)}
.flink{position:absolute;font-size:10px;color:var(--white);white-space:nowrap}
.copy{position:absolute;left:0;top:250px;width:100%;text-align:center;font-size:9px;color:#ddd}
</style>
</head>
<body>

<header>
  <div class="hero" role="img" aria-label="Photo of a traveller on a rock overlooking a tropical island bay, with clouds along the bottom"></div>
  <nav>
    <span class="nav active" style="left:117px">Home</span>
    <span class="nav" style="left:183px">About Me</span>
    <span class="nav" style="left:263px">Why Book With Us?</span>
    <span class="nav" style="left:390px">Blog</span>
    <span class="nav" style="left:446px">Let's Connect</span>
    <div class="brand" style="left:540px;top:12px;width:120px">
      <div style="width:38px;height:38px;margin:0 auto 4px;border-radius:50%;background:var(--teal)"></div>
      <div style="font-size:11px;line-height:13px">JOURNEY WITH MEREL</div>
    </div>
    <span class="nav" style="left:692px">FAQs</span>
    <span class="nav" style="left:755px">Forms &amp; Questionnaires</span>
    <span class="social" style="left:888px"></span>
    <span class="social" style="left:916px"></span>
    <a class="btn-outline">Book Your Trip</a>
  </nav>
  <p class="tagline">Let's Create Best Memories All Over The World</p>
  <h1 class="hero-title">Travel World</h1>

  <form class="search">
    <div class="field" style="width:220px;padding-left:50px"><div class="lbl"><i></i>State of Residence</div><div class="val">Select Your State <span style="margin-left:34px;color:#999">⌄</span></div></div>
    <div class="field" style="width:165px;padding-left:37px"><div class="lbl"><i></i>Total Trip Cost</div><div class="val">$&nbsp;&nbsp; 000,00.000</div></div>
    <div class="field" style="width:165px;padding-left:30px"><div class="lbl"><i></i>Departure Date</div><div class="val">MM/DD/YYYY</div></div>
    <div class="field" style="width:360px;padding-left:45px;border-right:0"><div class="lbl"><i></i>Return Date</div><div class="val">MM/DD/YYYY</div></div>
    <span class="btn-teal" style="left:756px;top:24px;width:103px;height:44px">Search</span>
  </form>
</header>

<section class="about">
  <p class="eyebrow" style="top:814px">About Us</p>
  <h2 class="heading" style="top:840px">Who We Are?</h2>
  <p class="about-text" style="top:914px">Travel's in my blood! Growing up, my family owned a travel agency and, before I even knew I wanted to be a travel agent, I was off seeing the world—and gaining an appreciation for a well-planned trip. After graduating Northfield College of Travel Careers in 1996, I've held management positions with several internationally acclaimed travel companies, gaining a wealth of experience and knowledge that I put to good use when working with clients to design their trips.</p>
  <p class="about-text" style="top:1018px">In 2005, I moved from California to New Hampshire where I live with my husband and three sons on 3 beautiful acres. We have a massive vegetable garden, a budding orchard, 2 dogs and a flock of chickens for farm fresh eggs every day.</p>
  <div class="about-card">
    <h3>A Little About<br>Me &amp; Why You'll Like<br>Working With Me</h3>
    <p>I've Come Nose-to-nose With A Giraffe During An African Safari. I've Strolled Along The Ancient Pathways Of Machu Picchu And Walked Along The Great Wall Of China. I've Honeymooned In The Australian Outback. I've Stayed In Villas, Enjoyed All-inclusive Vacations, And Gone On Cruises And Escorted Bus Tours.</p>
  </div>
  <div class="about-photo" role="img" aria-label="Aerial photo of a harbour city with an opera house, bridge and a ferry on turquoise water"></div>
</section>

<section class="dest">
  <p class="eyebrow">Destinations</p>
  <h2 class="heading">Your Next Trip</h2>
  <div class="dcard" style="left:0;top:223px;width:160px;height:353px;background:linear-gradient(180deg,#9bb6c7,#6f8ea3 60%,#4b6170)" role="img" aria-label="Family on a beach vacation"><span style="text-align:left;left:20px;opacity:.6">Vacations</span></div>
  <div class="dcard" style="left:183px;top:223px;width:263px;height:353px;background:linear-gradient(180deg,#4b8fd0,#7fb2de 50%,#3c4b3e 100%)" role="img" aria-label="Eiffel Tower against a blue sky"><span>Custom Travel</span></div>
  <div class="dcard" style="left:469px;top:207px;width:263px;height:386px;background:linear-gradient(180deg,#3e5c88,#e0a34e 35%,#9a7a56 60%,#6b4a2e 100%)" role="img" aria-label="Hillside town with ancient ruins at sunset"></div>
  <div class="dcard" style="left:753px;top:223px;width:263px;height:353px;background:linear-gradient(180deg,#d8d0c2,#7fc6d6 50%,#a99b86 100%)" role="img" aria-label="Couple relaxing by a beach canopy"><span>Honeymoon &amp; Romance</span></div>
  <div class="dcard" style="left:1039px;top:223px;width:161px;height:353px;background:linear-gradient(180deg,#2f5f9a,#5b8fc2 50%,#1b6ea5 100%)" role="img" aria-label="Cruise ship at sea"><span style="opacity:.6">Cruises</span></div>
  <span class="arrow" style="left:146px;top:385px"><svg width="8" height="10" viewBox="0 0 8 10"><path d="M6 1 2 5l4 4" fill="none" stroke="#333" stroke-width="1.5"/></svg></span>
  <span class="arrow" style="left:1026px;top:385px"><svg width="8" height="10" viewBox="0 0 8 10"><path d="M2 1l4 4-4 4" fill="none" stroke="#333" stroke-width="1.5"/></svg></span>
</section>

<section class="ready" role="img" aria-label="Mountain lake landscape above the clouds with a passenger jet flying toward the viewer">
  <h2>Are You Ready For Your<br>Pack Up + Go Adventure?</h2>
  <span class="btn-teal" style="left:537px;top:240px;width:126px;height:42px">Book Your Trip</span>
</section>

<section class="blogs">
  <p class="eyebrow" style="top:2790px">Our Post</p>
  <h2 class="heading" style="top:2815px">Recent Blogs &amp; Post</h2>
  <article class="blog" style="left:95px;top:2942px;width:224px;height:302px;background:linear-gradient(180deg,#1d3a63,#5a7c9c 45%,#1a1a1a 100%)" role="img" aria-label="River cruise ship at dusk">
    <p class="t" style="top:235px">Linguine Pasta With Zucchini &amp; Vongole By Seabright...</p><span class="m" style="top:272px">Learn More</span></article>
  <article class="blog" style="left:336px;top:2910px;width:280px;height:370px;background:linear-gradient(180deg,#2e4a2f,#5a7a6e 40%,#6f8c91 60%,#1a1a1a 100%)" role="img" aria-label="Luxury yacht on green water">
    <p class="t" style="top:306px">Ocean Vs. River Cruising: Which One Is Right For You?</p><span class="m" style="top:344px">Learn More</span></article>
  <article class="blog" style="left:635px;top:2942px;width:225px;height:302px;background:linear-gradient(180deg,#cfd6dc,#9aa5ad 45%,#1e1e1e 100%)" role="img" aria-label="Traveller with backpack on a cliff">
    <p class="t" style="top:235px">The Secret To Having The Best Trip Of Your Life...</p><span class="m" style="top:272px">Learn More</span></article>
  <article class="blog" style="left:882px;top:2942px;width:224px;height:302px;background:linear-gradient(180deg,#3a7da6,#6fb4c4 40%,#1c2a20 100%)" role="img" aria-label="Palm trees on a Caribbean beach">
    <p class="t" style="top:255px">The Caribbean Is (Still) Calling</p><span class="m" style="top:272px">Learn More</span></article>
  <span class="arrow-teal" style="left:80px;top:3076px"><svg width="8" height="10" viewBox="0 0 8 10"><path d="M6 1 2 5l4 4" fill="none" stroke="#fff" stroke-width="1.5"/></svg></span>
  <span class="arrow-teal" style="left:1091px;top:3076px"><svg width="8" height="10" viewBox="0 0 8 10"><path d="M2 1l4 4-4 4" fill="none" stroke="#fff" stroke-width="1.5"/></svg></span>
</section>

<section class="insure">
  <div class="abs" style="inset:0" role="img" aria-label="Calm lake with forested shore and the bow of a boat with coiled rope"></div>
  <p class="eyebrow">Purchase Travel Insurance</p>
  <h2 class="heading">Harborline Travel Insurance</h2>
  <form class="form">
    <h4>Worry less about the unexpected.</h4>
    <span class="flabel" style="left:40px;top:62px">State of Residence</span>
    <span class="input" style="left:31px;top:77px;width:308px">Select Your State* <span style="margin-left:150px">⌄</span></span>
    <span class="flabel" style="left:366px;top:62px">Total Trip Cost</span>
    <span class="input" style="left:356px;top:77px;width:308px;padding-left:30px">$&nbsp;&nbsp;&nbsp; 000,00.000*</span>
    <span class="flabel" style="left:40px;top:139px">Departure Date</span>
    <span class="input" style="left:31px;top:154px;width:308px">MM/DD/YYYY*</span>
    <span class="flabel" style="left:366px;top:134px"><i class="radio" style="background:#fff"></i>Age &nbsp;&nbsp;&nbsp;&nbsp; <i class="radio"></i>Date of Birth</span>
    <span class="box" style="left:358px;top:154px"></span><span class="box" style="left:410px;top:154px"></span><span class="box" style="left:463px;top:154px"></span><span class="box" style="left:516px;top:154px"></span>
    <span class="flabel" style="left:40px;top:216px">Return Date</span>
    <span class="input" style="left:31px;top:231px;width:308px">MM/DD/YYYY*</span>
    <span class="flabel" style="left:366px;top:216px">Initial Deposit Date</span>
    <span class="input" style="left:356px;top:231px;width:308px">MM/DD/YYYY*</span>
    <span class="btn-teal" style="left:30px;top:318px;width:127px;height:42px">Get a Quote</span>
    <span class="badge" style="left:470px;top:318px"></span>
  </form>
</section>

<footer class="footer">
  <div class="abs" style="inset:0" role="img" aria-label="Hiker on a mountain ridge"></div>
  <div class="brand" style="left:145px;top:58px;width:135px">
    <div style="width:58px;height:58px;margin:0 auto 8px;border-radius:50%;background:var(--teal)"></div>
    <div style="font-size:14px;line-height:17px">JOURNEY WITH MEREL</div>
  </div>
  <span class="fcol-title" style="left:395px;top:60px">Quick Links</span>
  <span class="flink" style="left:397px;top:88px;color:var(--teal)">Home</span>
  <span class="flink" style="left:397px;top:106px">About Me</span>
  <span class="flink" style="left:397px;top:124px">Why Book With Us?</span>
  <span class="flink" style="left:397px;top:142px">Blog</span>
  <span class="flink" style="left:397px;top:160px">Let's Connect</span>
  <span class="fcol-title" style="left:585px;top:60px">Contact Us</span>
  <svg class="abs" style="left:585px;top:88px" width="10" height="10" viewBox="0 0 10 10"><path d="M2 1h2l1 2-1 1a5 5 0 0 0 2 2l1-1 2 1v2a1 1 0 0 1-1 1A8 8 0 0 1 1 2a1 1 0 0 1 1-1z" fill="#6FCCEA"/></svg>
  <span class="flink" style="left:605px;top:88px">555-014-2290</span>
  <svg class="abs" style="left:585px;top:110px" width="11" height="8" viewBox="0 0 11 8"><rect x=".5" y=".5" width="10" height="7" fill="none" stroke="#6FCCEA"/><path d="M.5.5 5.5 4.5l5-4" fill="none" stroke="#6FCCEA"/></svg>
  <span class="flink" style="left:605px;top:108px">info@journeywithmerel.example</span>
  <svg class="abs" style="left:585px;top:130px" width="9" height="12" viewBox="0 0 9 12"><path d="M4.5 11S1 7 1 4.5a3.5 3.5 0 0 1 7 0C8 7 4.5 11 4.5 11z" fill="#6FCCEA"/></svg>
  <span class="flink" style="left:605px;top:130px;line-height:13px">Lorem Ipsum is simply<br>dummy text of the printing</span>
  <span class="fcol-title" style="left:832px;top:60px">Subscribe Our Newsletter</span>
  <span class="flink" style="left:832px;top:84px;line-height:14px;color:#cfcfcf">Subscribe newsletter for the latest<br>offers and news</span>
  <span class="abs" style="left:832px;top:135px;width:168px;height:36px;background:#fff;font-size:9px;color:#999;padding:13px 0 0 22px">Enter Email..</span>
  <span class="btn-teal" style="left:1000px;top:135px;width:46px;height:36px"><svg width="14" height="8" viewBox="0 0 14 8"><path d="M0 4h12M9 1l3 3-3 3" fill="none" stroke="#fff"/></svg></span>
  <p class="copy">Copyright © 2024 · Journey with Merel LLC · All rates quoted on this website are subject to change without notice</p>
</footer>

</body>
</html>
```